Poster Design for kebab shop products

need a new poster for our new blazer tray special, sign will be inside of shopping centre at different location to shop will need to stand out and draw customers to the store, MUST contain shops logo & picture added, poster size will be 76cm x 101cm so will need to suit that size

MUST ALSO CONTAIN THE FOLLOWING
Blazer Tray / HSP
Lamb & Chips
Chicken & Chips
Beef & Chips
+ Can $15

Target Market(s)

new customers

Industry/Entity Type

Retail

Font styles to use
Sans Serif

Colors

Designer to choose colors to be used in the design.

Requirements
Must have
• company logo
• picture of blazr tray provided
• Blazer Tray / HSP
• Lamb & Chips
• Chicken & Chips
• Beef & Chips
• + Can $15

```html
<!DOCTYPE html>
<html lang="en">
<head>
<meta charset="utf-8">
<title>Blazer Tray Special – Skewer Haven</title>
<link rel="stylesheet" href="https://fonts.googleapis.com/css2?family=Montserrat:wght@900&family=Oswald:wght@600;700&display=swap">
<style>
  :root {
    --red-deep: #5c0006;
    --red-main: #9a0a12;
    --red-band: #6e0008;
    --white: #ffffff;
    --outline: #2a2a2a;
    --yellow: #ffd21c;
    --orange: #f7931e;
    --badge-red: #e0171c;
    --ink: #1a1a1a;
    --tray-light: #f2f2f0;
    --food-mid: #b07a3c;
  }
  * { margin: 0; padding: 0; box-sizing: border-box; }
  html, body { width: 799px; height: 1200px; overflow: hidden; background: var(--red-deep); }
  .poster {
    position: relative;
    width: 799px;
    height: 1200px;
    overflow: hidden;
    background: radial-gradient(ellipse at 50% 38%, var(--red-main) 0%, #7d050d 45%, var(--red-deep) 100%);
  }
  .brand {
    position: absolute;
    top: 38px;
    left: 0;
    width: 100%;
    display: flex;
    justify-content: center;
    align-items: center;
    gap: 14px;
  }
  .brand-dot {
    width: 46px;
    height: 46px;
    border-radius: 50%;
    background: var(--orange);
  }
  .brand-name {
    font-family: "Oswald", sans-serif;
    font-weight: 700;
    font-size: 44px;
    color: var(--white);
    letter-spacing: 1px;
  }
  .headline {
    position: absolute;
    top: 0;
    left: 0;
  }
  .headline text {
    font-family: "Montserrat", sans-serif;
    font-weight: 900;
    fill: var(--white);
    stroke: var(--outline);
    stroke-width: 5px;
    paint-order: stroke fill;
  }
  .product-photo {
    position: absolute;
    left: 115px;
    top: 455px;
    width: 540px;
    height: 495px;
    border-radius: 26px;
    background: radial-gradient(ellipse at 50% 62%, var(--food-mid) 0%, #d9c08a 38%, var(--tray-light) 62%, #e4e4e2 100%);
  }
  .special-badge {
    position: absolute;
    left: 490px;
    top: 480px;
  }
  .special-badge text {
    font-family: "Oswald", sans-serif;
    font-weight: 700;
    font-size: 40px;
    fill: var(--ink);
  }
  .offer-band {
    position: absolute;
    left: 0;
    top: 955px;
    width: 100%;
    height: 245px;
    background: var(--red-band);
  }
  .price-burst {
    position: absolute;
    left: 172px;
    top: 987px;
  }
  .price-burst text {
    font-family: "Oswald", sans-serif;
    font-weight: 700;
    font-style: italic;
    fill: var(--ink);
  }
  .offer-list {
    position: absolute;
    left: 316px;
    top: 995px;
    list-style: none;
    font-family: "Oswald", sans-serif;
    font-weight: 600;
    font-size: 28px;
    line-height: 33.5px;
    color: var(--white);
  }
  .offer-list li { display: flex; align-items: center; }
  .offer-list .arrow {
    width: 14px;
    height: 16px;
    margin-right: 10px;
    flex: none;
  }
  .offer-list .addon { padding-left: 24px; }
</style>
</head>
<body>
<main class="poster">
  <header class="brand">
    <span class="brand-dot"></span>
    <span class="brand-name">Skewer Haven</span>
  </header>

  <svg class="headline" width="799" height="450" viewBox="0 0 799 450">
    <text x="95" y="295" font-size="150" textLength="575" lengthAdjust="spacingAndGlyphs">BLAZER</text>
    <text x="125" y="432" font-size="150" textLength="535" lengthAdjust="spacingAndGlyphs">TRAY</text>
  </svg>

  <div class="product-photo" role="img" aria-label="Photo of the Blazer Tray: sliced kebab meat over chips with garlic and tomato sauce in an open white takeaway box"></div>

  <svg class="special-badge" width="240" height="150" viewBox="0 0 240 150">
    <polygon points="20,60 210,35 195,120 30,140" fill="var(--badge-red)"/>
    <polygon points="15,20 225,10 210,95 5,105" fill="var(--yellow)"/>
    <text x="115" y="76" text-anchor="middle">SPECIAL</text>
  </svg>

  <div class="offer-band"></div>

  <svg class="price-burst" width="126" height="126" viewBox="-63 -63 126 126">
    <polygon fill="var(--yellow)" stroke="#e8a400" stroke-width="2"
      points="60,0 49.1,9.8 55.4,23 41.6,27.8 42.4,42.4 27.8,41.6 23,55.4 9.8,49.1 0,60 -9.8,49.1 -23,55.4 -27.8,41.6 -42.4,42.4 -41.6,27.8 -55.4,23 -49.1,9.8 -60,0 -49.1,-9.8 -55.4,-23 -41.6,-27.8 -42.4,-42.4 -27.8,-41.6 -23,-55.4 -9.8,-49.1 0,-60 9.8,-49.1 23,-55.4 27.8,-41.6 42.4,-42.4 41.6,-27.8 55.4,-23 49.1,-9.8"/>
    <text x="-30" y="-2" font-size="22">$</text>
    <text x="-14" y="18" font-size="48">15</text>
  </svg>

  <ul class="offer-list">
    <li><svg class="arrow" viewBox="0 0 14 16"><polygon points="0,0 14,8 0,16 4,8" fill="var(--orange)"/></svg>LAMB &amp; CHIPS</li>
    <li><svg class="arrow" viewBox="0 0 14 16"><polygon points="0,0 14,8 0,16 4,8" fill="var(--orange)"/></svg>CHICKEN &amp; CHIPS</li>
    <li><svg class="arrow" viewBox="0 0 14 16"><polygon points="0,0 14,8 0,16 4,8" fill="var(--orange)"/></svg>BEEF &amp; CHIPS</li>
    <li class="addon">+ CAN</li>
  </ul>
</main>
</body>
</html>
```